Signage. Will be for store front. Building is on a corner lot. Lots of traffic.

Opening a new location for our landscape business with a garden store (boutique theme) which will have big pottery pots, house plants, ferns and orchids for sale.

And on the side lot of the store we will have bigger bulk items(contractors theme) landscape plants, sod, mulch, soil, rock for sale.

Sign is about 8’x6’

Target Market(s)

Home owners
Landscapers
Builders

Industry/Entity Type

Landscaping

Font styles to use
Sans Serif

Colors
9bcb3c

Requirements
Must have
• “ Installation and Delivery” is a big deal to let people know we do that
Nice to have
• Added a first rendition idea but don’t love it
Added a file with some words to play with
Need help with the words
Should not have
• ?

```html
<!DOCTYPE html>
<html lang="en">
<head>
<meta charset="utf-8">
<title>Fernhollow Gardens – Storefront Sign</title>
<link rel="stylesheet" href="https://fonts.googleapis.com/css2?family=Roboto:wght@700&family=Oswald:wght@500&family=Yellowtail&display=swap">
<style>
  :root {
    --backdrop: #e9eef1;
    --panel-white: #f3f3f3;
    --panel-grey-top: #e6e6e6;
    --panel-grey-bottom: #dadada;
    --brand-green: #7c9c3c;
    --script-green: #5b7a31;
    --banner-green: #566f2e;
    --frame-green: #4d6a2a;
    --ink: #1b1b1b;
    --banner-text: #f7f7f2;
  }

  html, body {
    margin: 0;
    padding: 0;
    width: 1200px;
    height: 900px;
    overflow: hidden;
    background: var(--backdrop);
  }

  .sign {
    position: absolute;
    left: 60px;
    top: 98px;
    width: 1080px;
    height: 704px;
    display: flex;
    flex-direction: column;
    box-shadow: 0 6px 24px rgba(0, 0, 0, 0.12);
  }

  .sign-face {
    position: relative;
    flex: 0 0 590px;
    display: flex;
    flex-direction: column;
  }

  .sign-frame {
    position: absolute;
    inset: 14px 14px 0 14px;
    border: 2px solid var(--frame-green);
    border-bottom: none;
    pointer-events: none;
  }

  .brand-area {
    flex: 0 0 262px;
    background: var(--panel-white);
    display: flex;
    align-items: center;
    justify-content: center;
    gap: 30px;
  }

  .brand-name {
    font-family: "Roboto", Arial, sans-serif;
    font-weight: 700;
    color: var(--brand-green);
    text-transform: uppercase;
    font-size: 88px;
    line-height: 0.98;
    letter-spacing: 4px;
    margin: 0;
  }

  .brand-name span { display: block; }

  .brand-dot {
    width: 110px;
    height: 110px;
    border-radius: 50%;
    background: var(--brand-green);
    flex: 0 0 auto;
  }

  .offer-area {
    flex: 1;
    background: linear-gradient(var(--panel-grey-top), var(--panel-grey-bottom));
    display: flex;
    flex-direction: column;
    align-items: center;
    padding-top: 36px;
    box-sizing: border-box;
  }

  .offer-line {
    font-family: "Roboto", Arial, sans-serif;
    font-weight: 700;
    color: var(--ink);
    font-size: 66px;
    line-height: 72px;
    letter-spacing: -1px;
    margin: 0;
    display: flex;
    align-items: center;
    gap: 22px;
  }

  .offer-line .divider {
    display: inline-block;
    width: 3px;
    height: 54px;
    background: var(--ink);
  }

  .welcome {
    font-family: "Yellowtail", cursive;
    color: var(--script-green);
    font-size: 96px;
    line-height: 1;
    margin: 14px 0 0;
  }

  .service-banner {
    flex: 1;
    background: var(--banner-green);
    display: flex;
    align-items: center;
    justify-content: center;
  }

  .service-banner p {
    font-family: "Oswald", "Arial Narrow", sans-serif;
    font-weight: 500;
    color: var(--banner-text);
    font-size: 64px;
    letter-spacing: 1px;
    margin: 0;
    text-transform: uppercase;
  }
</style>
</head>
<body>
  <section class="sign">
    <div class="sign-face">
      <div class="sign-frame"></div>
      <header class="brand-area">
        <h1 class="brand-name"><span>Fernhollow</span><span>Gardens</span></h1>
        <div class="brand-dot"></div>
      </header>
      <div class="offer-area">
        <p class="offer-line">SOD <span class="divider"></span> LANDSCAPE SUPPLY</p>
        <p class="offer-line">LAWN <span class="divider"></span> GARDEN <span class="divider"></span> NURSERY</p>
        <p class="welcome">Public Welcome!</p>
      </div>
    </div>
    <footer class="service-banner">
      <p>Installation and Delivery Available</p>
    </footer>
  </section>
</body>
</html>
```